Business Coach needs an elegant business card design

I need a business card design based around my logo for color and to look like a millionaire dollar coach. Incorporate the color of my logo with something creative and attractive that stands out. I am focused on high end companies and the card must look and feel that way.

Target Market(s)

High End Companies and Business Owners - Training People to become millionaires

Industry/Entity Type

Business

Requirements
Must have
• Front -
Logo (attached file) - Website (marlowkeeve.com) - Name (Marlow Keeve) Phone (555.201.7746) - Email (marlow@marlowkeeve.com) (My Title - Success Coach)
Back -
Slogan - Vision (see it) . Action (do it) . Transformation (be it)
Website - Learn More @ marlowkeeve.com

Creative High End Look!
Nice to have
Should not have
• Cheap standard look
nothing traditional

```html
<!DOCTYPE html>
<html lang="en">
<head>
<meta charset="utf-8">
<title>Marlow Keeve Coaching – Business Card</title>
<link href="https://fonts.googleapis.com/css2?family=Lato:wght@400;700;900&display=swap" rel="stylesheet">
<style>
  :root {
    --bg: #2b2b2d;
    --navy: #1b2350;
    --navy-dark: #141a3d;
    --paper: #f4f4f6;
    --paper-shade: #e3e3e7;
    --ink-grey: #55565c;
    --white: #ffffff;
    --rule: #1b2350;
  }
  * { margin: 0; padding: 0; box-sizing: border-box; }
  html, body {
    width: 1200px; height: 994px; overflow: hidden;
    background: var(--bg);
    font-family: "Lato", Arial, sans-serif;
  }
  .card {
    position: absolute;
    width: 540px; height: 309px;
    border-radius: 16px;
    box-shadow: 0 18px 40px rgba(0,0,0,.45);
    overflow: hidden;
  }
  .card--back {
    left: 110px; top: 120px;
    background: linear-gradient(135deg, var(--navy) 0%, var(--navy-dark) 100%);
    color: var(--white);
  }
  .card--front {
    left: 550px; top: 540px;
    background: linear-gradient(135deg, var(--white) 0%, var(--paper) 60%, var(--paper-shade) 100%);
    color: var(--navy);
  }
  .brand {
    position: absolute;
    display: flex; align-items: center; gap: 16px;
  }
  .brand__dot {
    width: 66px; height: 66px; border-radius: 50%;
    flex: none;
  }
  .brand__name {
    font-weight: 700;
    font-size: 26px;
    letter-spacing: 2px;
    line-height: 1.15;
    text-transform: uppercase;
  }
  .card--back .brand { left: 60px; top: 66px; }
  .card--back .brand__dot { background: var(--white); }
  .card--back .brand__name { color: var(--white); }
  .card--front .brand { left: 70px; top: 50px; }
  .card--front .brand__dot { background: var(--navy); }
  .card--front .brand__name { color: var(--navy); }

  .slogan {
    position: absolute; left: 150px; top: 180px;
    list-style: none;
    font-size: 15px; line-height: 1.8; letter-spacing: .3px;
  }
  .slogan__key { font-weight: 900; }

  .holder {
    position: absolute; left: 70px; top: 222px;
  }
  .holder__name {
    font-weight: 900; font-size: 19px; letter-spacing: .5px;
    text-transform: uppercase; color: var(--navy);
  }
  .holder__title {
    font-size: 16px; color: var(--ink-grey); margin-top: 2px;
  }
  .divider {
    position: absolute; left: 268px; top: 168px;
    width: 2px; height: 110px;
    background: linear-gradient(to bottom, transparent, var(--rule) 30%, var(--rule) 70%, transparent);
  }
  .contact {
    position: absolute; left: 290px; top: 176px;
    list-style: none;
    font-size: 14.5px; color: var(--ink-grey);
  }
  .contact li {
    display: flex; align-items: center; gap: 9px;
    margin-bottom: 10px;
  }
  .contact svg { width: 16px; height: 16px; flex: none; fill: var(--navy); }
  .contact__web { font-weight: 900; color: var(--navy); }
</style>
</head>
<body>

  <section class="card card--back" aria-label="Card back">
    <div class="brand">
      <span class="brand__dot"></span>
      <span class="brand__name">Marlow Keeve<br>Coaching</span>
    </div>
    <ul class="slogan">
      <li><span class="slogan__key">VISION</span> . See What You Want</li>
      <li><span class="slogan__key">ACTION</span> . Do What It Takes</li>
      <li><span class="slogan__key">TRANSFORMATION</span> . Live Your Vision!</li>
    </ul>
  </section>

  <section class="card card--front" aria-label="Card front">
    <div class="brand">
      <span class="brand__dot"></span>
      <span class="brand__name">Marlow Keeve<br>Coaching</span>
    </div>

    <div class="holder">
      <div class="holder__name">Marlow Keeve</div>
      <div class="holder__title">Success Coach</div>
    </div>

    <div class="divider"></div>

    <ul class="contact">
      <li>
        <svg viewBox="0 0 24 24" aria-hidden="true"><path d="M6.6 10.8a15.1 15.1 0 0 0 6.6 6.6l2.2-2.2c.3-.3.7-.4 1-.2 1.1.4 2.3.6 3.6.6.6 0 1 .4 1 1V20c0 .6-.4 1-1 1A17 17 0 0 1 3 4c0-.6.4-1 1-1h3.5c.6 0 1 .4 1 1 0 1.3.2 2.5.6 3.6.1.3 0 .7-.2 1z"/></svg>
        <span>555.201.7746</span>
      </li>
      <li>
        <svg viewBox="0 0 24 24" aria-hidden="true"><path d="M2 5h20v14H2z M3 6l9 7 9-7" fill="var(--navy)"/><path d="M3.5 6.5 12 13l8.5-6.5" fill="none" stroke="#fff" stroke-width="1.6"/></svg>
        <span>marlow@marlowkeeve.com</span>
      </li>
      <li>
        <span class="contact__web">www.marlowkeeve.com</span>
      </li>
    </ul>
  </section>

</body>
</html>
```